Whimsical sticker needed for heavenly microwave single serve cake/treat (mug cake)

Sticker design needed for a delicious microwaveable single serve cake. The amazingly cute sticker you design will be applied to the front of a 4"x5" white single serve pouch. We will add an additional flavor sticker to define each SKU, so your design just needs to represent the concept of a fresh baked "cake"-ready in a minute. (We have brownies, muffins, pancakes, and crumb cake varieties, so don't let the design limit the assortment of flavors/varieties please.)

Looking for something whimsical and fun, that appeals to both sexes, that are having a sweet tooth attack!

Warm Crumbs by Wilma is the brand name this product will be offered under.

Sticker size needs to be 3.8" x 3.8" please.

Excited to see what you come up with! Will send small logo once we decide on a design. ;-)

Attached is an image of a similar concept for comparison.

Our logo color is PMS 239. This is a link to our products packaging palette colors. https://www.huevaro.com/articles/color-palettes/vivify-a-cheerful-palette-expressing-freshness-and-positivity.

The other attachment is the background pattern design we use on other packaging.

Let's use your amazing talent, to make our fun concept really pop!

If adding cupcake illustrations, We like these: https://www.pixmarrow.com/vector/pattern-of-cartoon-cupcakes-on-white-isolated-background-cakes-as-a-vector-stock-gm1280936724-379114338 https://www.pixmarrow.com/vector/muffins-gm165632220-9555959 https://www.pixmarrow.com/vector/cartoon-muffins-set-gm513806304-87799445

Target Market(s)

Both women and men 21+ looking for a more upscale fun cannabis edibles than gummies.

Industry/Entity Type

Cannabis

Font styles to use
Serif
Other font styles liked:
• Match other packaging example if possible

Colors
e667a6
abd037
85acd3
e34197
b8a6cd
fbed22
9bcb3c

Requirements
Must have
• Clean & fresh design. See example of our bath product packaging which was uploaded as inspiration. Will provide logo shortly. Logo color is PMS 139. But not too much pink on this design, as we want it to appeal to men too.

Needs red THC warning symbol & Contains Marijuana. Keep away from Children. Font for this warning needs to be at minimum 1/16" Red symbol must be 1/2" tall.

Single Serving.

Need this sticker you are designing to be universal for all our flavors and THC strengths that we offer.
Nice to have
• Perhaps use little chef hat and mug with steam, similar to how we used graphics on the bath products - please see packaging example attached?

Directions like "Pour in a mug, add water, microwave, ENJOY!"

www.wilmoqex.com
Should not have
• No cannabis leaves or stereotypical stoner looking graphics please.

```html
<!DOCTYPE html>
<html lang="en">
<head>
<meta charset="utf-8">
<title>Warm Crumbs by Wilma – Mug Cake Sticker</title>
<link rel="stylesheet" href="https://fonts.googleapis.com/css2?family=Merriweather:wght@700;900&family=Kaushan+Script&family=Oswald:wght@500&display=swap">
<style>
  :root {
    --pink-deep: #d0479b;
    --pink-mid: #e08cbd;
    --pink-soft: #f0bcd9;
    --lime: #d3e27a;
    --lime-soft: #e4edb6;
    --green: #9bcb3c;
    --brand-pink: #c9408f;
    --thc-red: #e1252d;
    --white: #ffffff;
    --illustration-grey: #e7e8ec;
    --illustration-yellow: #f2e526;
  }
  html, body {
    margin: 0;
    padding: 0;
    width: 1197px;
    height: 1200px;
    overflow: hidden;
    background: var(--white);
  }
  .sticker {
    display: block;
    width: 1197px;
    height: 1200px;
  }
  .brand-tagline {
    font-family: "Merriweather", Georgia, serif;
    font-weight: 900;
    font-size: 25px;
    fill: var(--brand-pink);
  }
  .brand-name {
    font-family: "Merriweather", Georgia, serif;
    font-weight: 900;
    font-size: 64px;
    fill: var(--brand-pink);
  }
  .headline {
    font-family: "Merriweather", Georgia, serif;
    font-weight: 700;
    font-size: 41px;
    fill: var(--white);
  }
  .script-line {
    font-family: "Kaushan Script", cursive;
    font-size: 66px;
    fill: var(--white);
  }
  .warning-text {
    font-family: "Oswald", "Arial Narrow", sans-serif;
    font-weight: 500;
    font-size: 15px;
    fill: var(--white);
    letter-spacing: 0.2px;
  }
  .thc-label {
    font-family: "Oswald", "Arial Narrow", sans-serif;
    font-weight: 500;
    font-size: 24px;
    fill: var(--thc-red);
  }
  .directions {
    font-family: "Merriweather", Georgia, serif;
    font-weight: 700;
    font-size: 20px;
    fill: var(--white);
  }
  .web-address {
    font-family: "Merriweather", Georgia, serif;
    font-weight: 900;
    font-size: 26px;
    fill: var(--white);
    letter-spacing: 0.5px;
  }
</style>
</head>
<body>
<svg class="sticker" viewBox="0 0 1197 1200" xmlns="http://www.w3.org/2000/svg">
  <defs>
    <linearGradient id="ring-tones" x1="0" y1="0" x2="1" y2="1">
      <stop offset="0" stop-color="var(--pink-deep)"/>
      <stop offset="0.35" stop-color="var(--pink-mid)"/>
      <stop offset="0.6" stop-color="var(--lime-soft)"/>
      <stop offset="0.8" stop-color="var(--pink-soft)"/>
      <stop offset="1" stop-color="var(--lime)"/>
    </linearGradient>
    <clipPath id="outer-disc"><circle cx="589" cy="596" r="393"/></clipPath>
    <clipPath id="inner-disc"><circle cx="589" cy="596" r="334"/></clipPath>
    <path id="directions-arc" d="M 280 596 A 309 309 0 0 0 898 596"/>
    <path id="web-arc" d="M 237 596 A 352 352 0 0 0 941 596"/>
  </defs>

  <!-- Patterned border ring -->
  <path class="pattern-ring" role="img" aria-label="Decorative pink and lime quatrefoil tile pattern ring"
        fill="url(#ring-tones)" fill-rule="evenodd"
        d="M 196 596 A 393 393 0 1 0 982 596 A 393 393 0 1 0 196 596 Z
           M 255 596 A 334 334 0 1 1 923 596 A 334 334 0 1 1 255 596 Z"/>

  <!-- Bottom web band -->
  <rect class="web-band" x="150" y="886" width="900" height="150" fill="var(--pink-deep)" clip-path="url(#outer-disc)"/>

  <!-- Inner face: white header and green body -->
  <g clip-path="url(#inner-disc)">
    <rect class="header-panel" x="240" y="250" width="700" height="143" fill="var(--white)"/>
    <rect class="body-panel" x="240" y="393" width="700" height="550" fill="var(--green)"/>
  </g>

  <!-- Brand -->
  <text class="brand-tagline" x="578" y="308" text-anchor="middle">Warm Crumbs by</text>
  <text class="brand-name" x="570" y="372" text-anchor="middle">Wilma</text>
  <circle class="brand-dot" cx="705" cy="322" r="13" fill="var(--brand-pink)"/>

  <!-- Headline -->
  <text class="headline" x="589" y="456" text-anchor="middle">fresh baked cake</text>
  <text class="script-line" x="587" y="530" text-anchor="middle">ready in a minute</text>
  <path class="script-underline" d="M 672 546 Q 780 536 884 531" stroke="var(--white)" stroke-width="3" fill="none" stroke-linecap="round"/>

  <!-- Illustration area -->
  <rect class="kitchen-illustration" role="img"
        aria-label="Illustration of a chef hat, a whisk and a steaming yellow mug"
        x="487" y="560" width="206" height="150" rx="24" fill="var(--illustration-grey)" opacity="0.9"/>

  <!-- THC warning symbol -->
  <g class="thc-symbol">
    <path d="M 582 718 L 634 770 L 582 822 L 530 770 Z" fill="var(--white)" stroke="var(--thc-red)" stroke-width="5" stroke-linejoin="miter"/>
    <rect x="579" y="728" width="6" height="20" rx="1" fill="var(--thc-red)"/>
    <circle cx="582" cy="754" r="3.5" fill="var(--thc-red)"/>
    <text class="thc-label" x="582" y="783" text-anchor="middle">THC</text>
  </g>

  <!-- Warning -->
  <text class="warning-text" x="582" y="843" text-anchor="middle">CONTAINS MARIJUANA.</text>
  <text class="warning-text" x="582" y="863" text-anchor="middle">KEEP AWAY FROM CHILDREN.</text>

  <!-- Curved directions -->
  <text class="directions">
    <textPath href="#directions-arc" startOffset="50%" text-anchor="middle">Single Serving | Direction: Pour in a mug, add water, microwave, ENJOY!</textPath>
  </text>

  <!-- Curved web address -->
  <text class="web-address">
    <textPath href="#web-arc" startOffset="50%" text-anchor="middle">www.wilmoqex.com</textPath>
  </text>
</svg>
</body>
</html>
```